Realtor resource

This is a website that provides resources for Realtors and their customers (home buyers and sellers).

There are 5 pages that I need redesigned:

1. Homepage: https://brightkeyguide.example/
2. Support Page/Contact Us: https://brightkeyguide.example/contact-us/
3. Agent Dashboard - See attached screenshot
4. Real Estate Documents page - See attached screenshot
5. Real Estate Contract page - see attached screenshot

Target Market(s)

Real estate agents and their customers.

Industry/Entity Type

Real Estate

Number of Pages Required

5+ page

Requirements
Must have
• Please use a modern design and incorporate design with current logo.

```html
<!DOCTYPE html>
<html lang="en">
<head>
<meta charset="utf-8">
<title>BrightKey Guide – Home</title>
<link href="https://fonts.googleapis.com/css2?family=Poppins:wght@400;500;600&family=Roboto+Condensed:wght@400&display=swap" rel="stylesheet">
<style>
  :root{
    --orange:#f7941d;
    --orange-soft:#fbe6cf;
    --ink:#111111;
    --text:#1d1d1d;
    --bg-light:#f4f4f4;
    --bg-mid:#e4e4e4;
    --white:#ffffff;
  }
  *{box-sizing:border-box;margin:0;padding:0}
  html,body{width:1200px;height:567px;overflow:hidden;background:var(--white)}
  body{position:relative;font-family:"Poppins",sans-serif;color:var(--text)}
  .site-header{position:absolute;left:0;top:0;width:1200px;height:60px;background:var(--white);z-index:3}
  .brand{position:absolute;left:140px;top:15px;display:flex;align-items:center;gap:8px;font-size:22px;font-weight:600;color:var(--ink);text-decoration:none}
  .brand-dot{width:22px;height:22px;border-radius:50%;background:var(--orange)}
  .main-nav{position:absolute;top:22px;left:520px;display:flex;gap:21px;font-size:14px}
  .main-nav a{color:var(--text);text-decoration:none}
  .main-nav a.is-active{color:var(--orange);font-weight:500}
  .login-btn{position:absolute;left:942px;top:20px;width:117px;height:27px;border-radius:14px;background:var(--orange);color:var(--white);font-size:13px;display:flex;align-items:center;justify-content:center;gap:6px;text-decoration:none}
  .hero-bg{position:absolute;left:0;top:60px;width:1200px;height:340px;z-index:0}
  .hero-title{position:absolute;left:0;top:130px;width:1200px;text-align:center;font-family:"Roboto Condensed",sans-serif;font-size:31px;line-height:45px;color:var(--ink);z-index:2}
  .audience{position:absolute;width:208px;height:208px;border-radius:50%;background:var(--orange-soft);z-index:2;text-decoration:none}
  .audience .disc{position:absolute;left:12px;top:12px;width:184px;height:184px;border-radius:50%;background:var(--ink)}
  .audience svg.ring{position:absolute;left:0;top:0}
  .audience .icon{position:absolute;left:72px;top:48px;width:64px;height:64px;border-radius:10px;background:var(--orange);opacity:.9}
  .audience .label{position:absolute;left:0;width:208px;top:130px;text-align:center;color:var(--orange);font-weight:600;font-size:15px}
  .audience.agents{left:330px;top:263px}
  .audience.clients{left:597px;top:263px}
  .social{position:absolute;top:495px;left:0;width:1200px;display:flex;justify-content:center;align-items:center;gap:10px;font-size:13px;z-index:2}
  .social-dot{width:26px;height:26px;border-radius:50%;background:#3b5ea8;border:2px solid #d9e3f3}
  .social-dot.sky{background:#2a9ad8}
  .social-dot.deep{background:#1f6fa8}
  .copyright{position:absolute;top:531px;left:0;width:1200px;text-align:center;font-size:13px;z-index:2}
  .copyright span{color:var(--orange)}
</style>
</head>
<body>
  <header class="site-header">
    <a class="brand" href="https://brightkeyguide.example/"><span>BrightKey Guide</span><span class="brand-dot"></span></a>
    <nav class="main-nav">
      <a class="is-active" href="https://brightkeyguide.example/">Home</a>
      <a href="#">Support</a>
      <a href="#">Real Estate Documents</a>
      <a href="https://brightkeyguide.example/contact-us/">Contact Us</a>
    </nav>
    <a class="login-btn" href="#">
      <svg width="14" height="14" viewBox="0 0 14 14" fill="none" stroke="#fff" stroke-width="1.4"><circle cx="7" cy="7" r="6"/><path d="M3.5 7h6M7 4.5 9.5 7 7 9.5"/></svg>
      Login Here
    </a>
  </header>

  <svg class="hero-bg" width="1200" height="340" viewBox="0 0 1200 340" role="img" aria-label="Soft grey faceted background">
    <defs>
      <linearGradient id="heroGrad" x1="0" y1="0" x2="1" y2="1">
        <stop offset="0" stop-color="var(--bg-mid)"/>
        <stop offset=".5" stop-color="var(--bg-light)"/>
        <stop offset="1" stop-color="var(--bg-mid)"/>
      </linearGradient>
    </defs>
    <path d="M0 0H1200V265Q600 405 0 265Z" fill="url(#heroGrad)"/>
    <path d="M0 265Q600 405 1200 265" fill="none" stroke="var(--orange)" stroke-width="3"/>
  </svg>

  <h1 class="hero-title">Real Estate Contracts Explained In Plain Language<br>By Texas Real Estate Attorneys</h1>

  <a class="audience agents" href="#">
    <span class="disc"></span>
    <svg class="ring" width="208" height="208"><circle cx="104" cy="104" r="85" fill="none" stroke="var(--orange)" stroke-width="1.5" stroke-dasharray="6 4"/></svg>
    <span class="icon" role="img" aria-label="Agent with house icon"></span>
    <span class="label">Agents</span>
  </a>
  <a class="audience clients" href="#">
    <span class="disc"></span>
    <svg class="ring" width="208" height="208"><circle cx="104" cy="104" r="85" fill="none" stroke="var(--orange)" stroke-width="1.5" stroke-dasharray="6 4"/></svg>
    <span class="icon" role="img" aria-label="Buyers and sellers icon"></span>
    <span class="label">Buyers &amp; Sellers</span>
  </a>

  <div class="social">
    <span>Follow Us On</span>
    <span class="social-dot"></span>
    <span class="social-dot sky"></span>
    <span class="social-dot deep"></span>
  </div>
  <p class="copyright">Copyright © 2019 BrightKey Guide<span>.</span>&nbsp; All Rights Reserved.</p>
</body>
</html>
```